Clothing for elderly and disabled persons business card

I have seen a design on the Prism website with a partial hand holding a heart I would like that to be incorporated above the i in Willowmere
The colours should be either soft green and pinks.
The final design should communicate care, love, easy fit comfort clothing for the frail and disabled.

Willowmere
Gentle WearClothing

Target Market(s)

Nursing Homes, Elderly in care or just anyone with limited mobility

Industry/Entity Type

Clothing

Contact Information for Business Card

Willowmere Gentle Wear Clothing
Carol Hensley Owner Sales Consultant
Phone 0451 726 083 Fax 08 9627 4418
Email: willowmeregentlewear@examplemail.com

Requirements
Nice to have
• A hand holding a heart this must form part of the i in Willowmere, instead of the dot above the i I want the hand holding the heart.

```html
<!DOCTYPE html>
<html lang="en">
<head>
<meta charset="utf-8">
<title>Willowmere Gentle Wear Clothing – Business Card</title>
<link rel="stylesheet" href="https://fonts.googleapis.com/css2?family=Tinos:ital,wght@0,400;0,700;1,400&display=swap">
<style>
  :root {
    --page: #ffffff;
    --card: #ffffff;
    --card-edge: #5a5a5a;
    --soft-green: #b5d88d;
    --soft-pink: #f18fbb;
    --serif: "Tinos", "Times New Roman", serif;
  }
  * { margin: 0; padding: 0; box-sizing: border-box; }
  html, body {
    width: 1200px;
    height: 1000px;
    overflow: hidden;
    background: var(--page);
    font-family: var(--serif);
  }
  .canvas { position: relative; width: 1200px; height: 1000px; }
  .card {
    position: absolute;
    left: 379px;
    width: 452px;
    height: 258px;
    background: var(--card);
    border: 1px solid var(--card-edge);
    border-radius: 14px;
    box-shadow: 0 2px 6px rgba(0,0,0,0.35);
    overflow: hidden;
  }
  .card--front { top: 215px; }
  .card--back { top: 527px; }

  .brand {
    position: absolute;
    left: 0; right: 0;
    top: 78px;
    text-align: center;
  }
  .brand__name {
    color: var(--soft-green);
    font-weight: 700;
    font-size: 45px;
    line-height: 50px;
    letter-spacing: 0.5px;
    text-transform: uppercase;
  }
  .brand__tagline {
    color: var(--soft-pink);
    font-weight: 700;
    font-size: 25px;
    line-height: 30px;
    margin-top: 2px;
  }

  .contact-person {
    position: absolute;
    left: 46px;
    top: 41px;
    color: var(--soft-pink);
  }
  .contact-person__name { font-weight: 700; font-size: 17px; line-height: 20px; }
  .contact-person__role { font-style: italic; font-size: 12px; line-height: 16px; }

  .contact-list {
    position: absolute;
    left: 46px;
    top: 139px;
    color: var(--soft-pink);
    font-size: 14px;
    line-height: 19px;
    border-collapse: collapse;
  }
  .contact-list td { padding: 0; white-space: nowrap; vertical-align: baseline; }
  .contact-list__label { font-weight: 400; width: 52px; }
  .contact-list__value { font-weight: 700; }
  .contact-list__value--small { font-size: 12.5px; }

  .care-illustration {
    position: absolute;
    left: 340px;
    top: 82px;
    width: 108px;
    height: 176px;
    border-radius: 40px 40px 0 0;
    background: linear-gradient(180deg, var(--soft-pink) 0%, var(--soft-pink) 42%, var(--soft-green) 60%, var(--soft-green) 100%);
  }
</style>
</head>
<body>
<main class="canvas">
  <section class="card card--front" aria-label="Business card front">
    <div class="brand">
      <div class="brand__name">Willowmere</div>
      <div class="brand__tagline">Gentle Wear Clothing</div>
    </div>
  </section>

  <section class="card card--back" aria-label="Business card back">
    <div class="contact-person">
      <div class="contact-person__name">Carol Hensley</div>
      <div class="contact-person__role">Owner-Sales Consultant</div>
    </div>
    <table class="contact-list">
      <tr><td class="contact-list__label">Phone</td><td class="contact-list__value">- 0451 726 083</td></tr>
      <tr><td class="contact-list__label">Fax</td><td class="contact-list__value">- 08 9627 4418</td></tr>
      <tr><td class="contact-list__label">Email</td><td class="contact-list__value contact-list__value--small">- willowmeregentlewear@examplemail.com</td></tr>
      <tr><td class="contact-list__label">Website</td><td class="contact-list__value">- www.willowmeregentlewear.com</td></tr>
    </table>
    <div class="care-illustration" role="img" aria-label="Illustration of two green hands holding up a large pink heart"></div>
  </section>
</main>
</body>
</html>
```